TBR CONTRACTING

I am looking for a logo/design for my business. Would like some unique symbol, would also like it to be double sided. On the back perhaps 3 pictures of some work we have done. I will attach some photos.

I would also like the colours to be orange and black or a dark grey and Orange.

Only writing I would like to see are:

(Contact number) 416-382-7146
(Name) Lewis Pardoe
(Email) lpardoe@quillmail.ca

Industry/Entity Type

Business

```html
<!DOCTYPE html>
<html lang="en">
<head>
<meta charset="utf-8">
<title>TBR Contracting – Business Card</title>
<link rel="stylesheet" href="https://fonts.googleapis.com/css2?family=Marcellus&family=Cormorant+Garamond:wght@500&family=Lato:wght@400&display=swap">
<style>
  :root {
    --bg: #ecebe8;
    --white: #ffffff;
    --orange: #e8622a;
    --ink: #1d1d1d;
    --rule: #2a2a2a;
    --photo-warm: #6e4128;
    --photo-light: #d9d6cf;
  }
  * { margin: 0; padding: 0; box-sizing: border-box; }
  html, body { width: 1200px; height: 800px; overflow: hidden; }
  body {
    background: var(--bg);
    display: flex;
    align-items: center;
    justify-content: center;
    gap: 40px;
  }
  .card {
    position: relative;
    width: 560px;
    height: 320px;
    overflow: hidden;
    box-shadow: 0 6px 18px rgba(0,0,0,0.18);
  }

  .wordmark {
    font-family: "Marcellus", serif;
    font-size: 36px;
    letter-spacing: 1px;
    color: var(--ink);
    white-space: nowrap;
    line-height: 1;
  }

  /* Back side: project photo */
  .card--back .project-photo {
    position: absolute;
    inset: 0;
    background: linear-gradient(115deg, var(--photo-light) 0%, #bdb6aa 32%, #93674a 58%, var(--photo-warm) 100%);
  }
  .card--back .wordmark {
    position: absolute;
    right: 28px;
    bottom: 36px;
    font-size: 32px;
    color: var(--white);
  }

  /* Front side: contact details */
  .card--front { background: var(--orange); }
  .card--front .brand-band {
    position: absolute;
    left: 0; top: 0;
    width: 100%;
    height: 128px;
    background: var(--white);
    border-bottom: 5px solid var(--rule);
    display: flex;
    align-items: center;
    justify-content: center;
    gap: 14px;
  }
  .brand-mark {
    width: 28px;
    height: 28px;
    background: var(--orange);
    flex: none;
  }
  .contact {
    position: absolute;
    left: 0;
    top: 150px;
    width: 100%;
    text-align: center;
    color: var(--ink);
  }
  .contact__name {
    font-family: "Cormorant Garamond", serif;
    font-weight: 500;
    font-size: 30px;
    line-height: 1;
  }
  .contact__role {
    font-family: "Cormorant Garamond", serif;
    font-weight: 500;
    font-size: 16px;
    margin-top: 2px;
  }
  .contact__line {
    font-family: "Lato", sans-serif;
    font-size: 19px;
    margin-top: 12px;
  }
  .contact__line--phone { margin-top: 18px; }
</style>
</head>
<body>
  <section class="card card--back">
    <div class="project-photo" role="img" aria-label="Photo of a finished living room and kitchen with wood cabinetry and large windows"></div>
    <div class="wordmark">TBR CONTRACTING</div>
  </section>

  <section class="card card--front">
    <header class="brand-band">
      <span class="brand-mark"></span>
      <span class="wordmark">TBR CONTRACTING</span>
    </header>
    <div class="contact">
      <p class="contact__name">Lewis Pardoe</p>
      <p class="contact__role">Project Manager</p>
      <p class="contact__line contact__line--phone">416-382-7146</p>
      <p class="contact__line">lpardoe@quillmail.ca</p>
    </div>
  </section>
</body>
</html>
```